Wordpress site needed for company's Healthcare Web App

Healthcare web app needs wordpress web design for web site that provides an overview of the product, a page explaining key features, a blog, a press release announcement section, customer testimonials, contact us, sign up page, invite friends.

The website should use the color scheme including in the logo. This web site is not the app, this website will be used to introduce the app.

Target Market(s)

Doctors, enterprise healthcare professionals, patients who will use patient portals to access their health info. (not the app itself, but this site introduces the app)

Industry/Entity Type

Health Care

Coding

Coded - Design and coding required

Number of Pages Required

5+ page

Font styles to use
Sans Serif

Requirements
Must have
• This is a Wordpress based site.
• Product Overview, Key Product Features, Blog, Press Releases, Events, Embedded Videos explaining the product and demo'ing features, Sign Up Page for people interested,
Nice to have
• Uplifting Hero Image for Healthcare Tech, color scheme fitting with logo

```html
<!DOCTYPE html>
<html lang="en">
<head>
<meta charset="utf-8">
<title>CareLedger – Healthcare App</title>
<link rel="stylesheet" href="https://fonts.googleapis.com/css2?family=Lato:wght@400;700&family=Open+Sans:wght@400;600&display=swap">
<style>
:root{
  --teal:#2087a3;
  --teal-dark:#1b7690;
  --ink:#2e2e2e;
  --muted:#6b6b6b;
  --soft:#f2f4f4;
  --line:#d9dddd;
  --white:#ffffff;
  --black:#1b1b1b;
}
*{box-sizing:border-box;margin:0;padding:0}
html,body{width:1200px;height:3543px;overflow:hidden}
body{position:relative;background:var(--white);font-family:"Open Sans",Arial,sans-serif;color:var(--ink)}
h1,h2,h3,h4{font-weight:400}
.abs{position:absolute}
.heading{font-family:"Lato",Arial,sans-serif;font-weight:400;color:var(--ink);letter-spacing:.5px}
.section-title{position:absolute;left:0;width:1200px;text-align:center;font-family:"Lato",Arial,sans-serif;font-size:36px;font-weight:400;color:var(--ink)}
.body-text{font-size:11.5px;line-height:24px;color:var(--muted)}
.btn-outline{position:absolute;display:flex;align-items:center;justify-content:center;border:1.5px solid #444;border-radius:4px;font-size:11px;font-weight:600;color:#333;letter-spacing:.3px}
.btn-solid{position:absolute;display:flex;align-items:center;justify-content:center;background:var(--teal);color:var(--white);border-radius:3px;font-size:13px;font-weight:600;letter-spacing:.5px}

/* header */
.topline{left:0;top:0;width:1200px;height:5px;background:var(--teal)}
.header{left:0;top:5px;width:1200px;height:123px;background:var(--white);box-shadow:0 2px 6px rgba(0,0,0,.08);z-index:2}
.brand{left:132px;top:28px;display:flex;align-items:center;gap:14px}
.brand-mark{width:46px;height:46px;background:var(--teal);border-radius:6px}
.brand-name{font-family:"Lato",Arial,sans-serif;font-size:34px;font-weight:700;color:var(--teal)}
.invite{left:954px;top:30px;width:114px;height:34px;font-size:11px;border-radius:3px}
.nav{left:600px;top:88px;display:flex;gap:0;font-size:11px;color:#555;letter-spacing:.3px}
.nav span{padding:0 17px;height:40px}
.nav .active{color:var(--teal);border-bottom:2px solid var(--teal)}

/* hero */
.hero{left:0;top:128px;width:1200px;height:446px;background:linear-gradient(90deg,#f7f7f7 0%,#eef0f1 35%,#c9d2d8 60%,#8ea6b6 80%,#b7c7d2 100%)}
.hero-title{left:132px;top:252px;font-size:42px;font-weight:700;font-family:"Lato",Arial,sans-serif;color:#333}
.hero-text{left:132px;top:318px;width:340px;font-size:11px;line-height:22px;color:#555}
.hero-signup{left:132px;top:387px;width:114px;height:43px}
.dots{left:132px;top:460px;display:flex;gap:6px}
.dots i{width:9px;height:9px;border-radius:50%;background:#bbb;display:block}
.dots i:first-child{background:var(--teal)}

/* overview */
.overview-art{left:0;top:574px;width:586px;height:529px;background:linear-gradient(160deg,#ffffff 0%,#f1f3f6 60%,#e2e6ec 100%)}
.overview-title{left:566px;top:708px;font-size:36px}
.overview-text{left:566px;top:774px;width:502px}
.overview-btn{left:565px;top:879px;width:115px;height:43px}

/* features */
.features{left:0;top:1103px;width:1200px;height:650px;background:var(--soft)}
.feature{position:absolute;width:320px}
.feature svg{position:absolute;left:0;top:0}
.feature h3{position:absolute;left:59px;top:0;font-family:"Lato",Arial,sans-serif;font-weight:400;font-size:19px;line-height:29px;color:#333}
.feature p{position:absolute;left:59px;top:72px;width:180px;font-size:10.5px;line-height:24px;color:var(--muted)}

/* blog */
.blog-img{height:182px;background:linear-gradient(135deg,#e8eef2,#bfcfd9 60%,#dfe6ea)}
.blog-title{font-family:"Lato",Arial,sans-serif;font-weight:400;font-size:19px;line-height:28px;color:#333}
.blog-text{width:340px;font-size:10.5px;line-height:24px;color:var(--muted)}

/* press */
.press{left:0;top:2213px;width:1200px;height:555px;background:var(--soft)}
.press-img{left:132px;top:2376px;width:416px;height:307px;background:linear-gradient(120deg,#dce6ec,#b7c6d1 55%,#eef2f4)}
.press-card{left:548px;top:2376px;width:517px;height:310px;background:var(--white);box-shadow:0 4px 14px rgba(0,0,0,.18)}

/* testimonial */
.avatar{left:562px;top:2903px;width:76px;height:76px;border-radius:50%;background:linear-gradient(160deg,#c9a58a,#7a5a48)}
.quote{left:200px;top:3004px;width:800px;text-align:center;font-size:11px;line-height:22px;color:var(--muted)}
.cite{left:0;top:3062px;width:1200px;text-align:center;font-size:13px;font-style:italic;color:var(--teal)}

/* newsletter */
.newsletter{left:0;top:3153px;width:1200px;height:109px;background:var(--teal)}
.newsletter-title{left:132px;top:3190px;font-family:"Lato",Arial,sans-serif;font-weight:400;font-size:29px;color:var(--white)}
.field{height:40px;border:1.5px solid rgba(255,255,255,.75);color:var(--white);font-size:12px;padding:0 14px;display:flex;align-items:center}
.submit{left:940px;top:3189px;width:128px;height:40px;background:var(--black);color:var(--white);font-size:14px;display:flex;align-items:center;justify-content:center;letter-spacing:.5px}

/* footer */
.footer{left:0;top:3262px;width:1200px;height:281px;background:var(--soft)}
.foot-h{font-family:"Lato",Arial,sans-serif;font-weight:400;font-size:20px;color:#333}
.foot-list{font-size:11px;line-height:24px;color:#444;list-style:none}
.contact-row{display:flex;align-items:flex-start;gap:14px;font-size:11px;line-height:16px;color:#444;margin-bottom:9px}
.contact-row svg{flex:none;margin-top:1px}
.map{left:777px;top:3302px;width:288px;height:165px;background:linear-gradient(135deg,#e6e4dc,#d6dcd2 50%,#e9e6dd)}
.foot-rule{left:132px;top:3491px;width:936px;height:1px;background:var(--line)}
.copy{left:0;top:3504px;width:1200px;text-align:center;font-size:10.5px;color:#555}
</style>
</head>
<body>

<div class="abs topline"></div>
<header class="abs header">
  <div class="abs brand"><span class="brand-mark"></span><span class="brand-name">CareLedger</span></div>
  <div class="btn-solid invite">INVITE FRIENDS</div>
  <nav class="abs nav">
    <span class="active">HOME</span><span>ABOUT US</span><span>SERVICES</span><span>PRESS</span><span>BLOG</span><span>CONTACT US</span>
  </nav>
</header>

<section class="abs hero" role="img" aria-label="Doctor touching a glowing interface of hexagonal healthcare icons"></section>
<h1 class="abs hero-title">HEALTHCARE APP</h1>
<p class="abs hero-text">Nemo enim ipsam voluptatem quia voluptas sit aspernatur aut odit aut fugit, sed quia consequuntur</p>
<div class="btn-solid hero-signup">SIGNUP</div>
<div class="abs dots"><i></i><i></i><i></i></div>

<div class="abs overview-art" role="img" aria-label="Stethoscope on a white background"></div>
<h2 class="abs heading overview-title">OVERVIEW OF THE PRODUCT</h2>
<p class="abs body-text overview-text">Nemo enim ipsam voluptatem quia voluptas sit aspernatur aut odit aut fugit, sed quia consequuntur magni dolores eos qui ratione voluptatem sequi nesciunt. Neque porro quisquam est, qui dolorem ipsum quia dolor sit amet, consectetur, adipisci velit, sed quia</p>
<div class="btn-outline overview-btn">VIEW DETAILS</div>

<section class="abs features">
  <h2 class="section-title" style="top:80px">KEY FEATURES</h2>
  <div class="feature" style="left:130px;top:208px">
    <svg width="34" height="40" viewBox="0 0 34 40" fill="none" stroke="#2087a3" stroke-width="3"><rect x="3" y="8" width="28" height="30"/><path d="M17 1v10M12 6h10"/><path d="M10 18h4M20 18h4M10 26h4M20 26h4M14 38v-6h6v6"/></svg>
    <h3>LOREM IPSUM<br>DOLOR</h3>
    <p>Nemo enim ipsam voluptatem quia voluptas sit aspernatur aut odit aut fugit, sed quia</p>
  </div>
  <div class="feature" style="left:472px;top:208px">
    <svg width="44" height="40" viewBox="0 0 44 40" fill="none" stroke="#2087a3" stroke-width="3"><rect x="7" y="8" width="30" height="20"/><path d="M2 32h40"/></svg>
    <h3>LOREM IPSUM<br>DOLOR</h3>
    <p>Nemo enim ipsam voluptatem quia voluptas sit aspernatur aut odit aut fugit, sed quia</p>
  </div>
  <div class="feature" style="left:812px;top:208px">
    <svg width="42" height="40" viewBox="0 0 42 40"><path d="M14 10V5h14v5" fill="none" stroke="#2087a3" stroke-width="3"/><rect x="2" y="10" width="38" height="28" rx="3" fill="#2087a3"/><path d="M21 16v16M13 24h16" stroke="#fff" stroke-width="4"/></svg>
    <h3>LOREM IPSUM<br>DOLOR</h3>
    <p>Nemo enim ipsam voluptatem quia voluptas sit aspernatur aut odit aut fugit, sed quia</p>
  </div>
  <div class="feature" style="left:130px;top:416px">
    <svg width="40" height="40" viewBox="0 0 40 40" fill="none" stroke="#2087a3" stroke-width="3" stroke-linejoin="round"><rect x="3" y="17" width="8" height="19"/><path d="M11 19l7-13c3 0 4 2 4 5l-1 6h12c2 0 4 2 3 4l-3 12c-1 2-2 3-4 3H11"/></svg>
    <h3>LOREM IPSUM<br>DOLOR</h3>
    <p>Nemo enim ipsam voluptatem quia voluptas sit aspernatur aut odit aut fugit, sed quia</p>
  </div>
  <div class="feature" style="left:472px;top:416px">
    <svg width="42" height="40" viewBox="0 0 42 40"><path d="M2 20C4 9 12 4 21 4s17 5 19 16c-3-3-6-3-9 0-3-3-7-3-10 0-3-3-7-3-10 0-3-3-6-3-9 0z" fill="#2087a3"/><path d="M21 20v13c0 4 -6 4 -6 0" fill="none" stroke="#2087a3" stroke-width="3"/></svg>
    <h3>LOREM IPSUM<br>DOLOR</h3>
    <p>Nemo enim ipsam voluptatem quia voluptas sit aspernatur aut odit aut fugit, sed quia</p>
  </div>
  <div class="feature" style="left:812px;top:416px">
    <svg width="40" height="40" viewBox="0 0 40 40" fill="none" stroke="#2087a3" stroke-width="3"><circle cx="20" cy="20" r="17"/><circle cx="20" cy="20" r="8"/><path d="M8 8l6 6M32 8l-6 6M8 32l6-6M32 32l-6-6"/></svg>
    <h3>LOREM IPSUM<br>DOLOR</h3>
    <p>Nemo enim ipsam voluptatem quia voluptas sit aspernatur aut odit aut fugit, sed quia</p>
  </div>
</section>

<h2 class="section-title" style="top:1825px">RECENT BLOG</h2>
<div class="abs blog-img" style="left:132px;top:1939px;width:206px" role="img" aria-label="Doctor working at a computer"></div>
<h3 class="abs blog-title" style="left:371px;top:1933px">LOREM IPSUM<br>DOLOR</h3>
<p class="abs blog-text" style="left:363px;top:1999px">Lorem ipsum dolor sit amet, consectetur adipisicing elit, sed do eiusmod tempor incididunt ut labore et dolore magna aliqua.</p>
<div class="btn-outline" style="left:366px;top:2091px;width:91px;height:38px;font-size:10px">READ MORE</div>
<div class="abs blog-img" style="left:624px;top:1939px;width:205px" role="img" aria-label="Team of smiling medical staff"></div>
<h3 class="abs blog-title" style="left:862px;top:1933px">LOREM IPSUM<br>DOLOR</h3>
<p class="abs blog-text" style="left:857px;top:1999px;width:212px">Lorem ipsum dolor sit amet, consectetur adipisicing elit, sed do eiusmod tempor incididunt ut labore et dolore magna aliqua.</p>
<div class="btn-outline" style="left:857px;top:2091px;width:91px;height:38px;font-size:10px">READ MORE</div>

<section class="abs press">
  <h2 class="section-title" style="top:60px">PRESS RELEASE</h2>
</section>
<div class="abs press-img" role="img" aria-label="Doctor with a laptop touching a digital interface"></div>
<div class="abs press-card">
  <h3 class="abs heading" style="left:40px;top:54px;font-size:23px">HEALTHCARE APP</h3>
  <p class="abs body-text" style="left:40px;top:110px;width:440px;font-size:10.5px">For paid search this is great news. This new longer ad format will look more like the SEO results and will finally give an opportunity to differentiate brands in the search results. The previous restrictions have meant that paid search</p>
  <div class="btn-outline" style="left:40px;top:216px;width:103px;height:40px">READ MORE</div>
</div>

<h2 class="section-title" style="top:2829px">CLIENT TESTIMONIALS</h2>
<div class="abs avatar" role="img" aria-label="Client portrait"></div>
<p class="abs quote">Ut enim ad minima veniam, quis nostrum exercitationem ullam corporis suscipit laboriosam, nisi ut aliquid ex ea commodi consequatur? Quis autem vel eum iure reprehenderit qui in ea voluptate velit esse quam nihil molestiae consequatur.</p>
<p class="abs cite">- Jane Rowe -</p>

<section class="abs newsletter"></section>
<h2 class="abs newsletter-title">NEWSLETTER SIGNUP</h2>
<div class="abs field" style="left:463px;top:3189px;width:224px">Name</div>
<div class="abs field" style="left:701px;top:3189px;width:227px">Email</div>
<div class="abs submit">SUBMIT</div>

<footer class="abs footer"></footer>
<h4 class="abs foot-h" style="left:132px;top:3304px">SITEMAP</h4>
<ul class="abs foot-list" style="left:132px;top:3340px"><li>Home</li><li>About us</li><li>Services</li><li>Press</li><li>Blog</li><li>contact us</li></ul>
<h4 class="abs foot-h" style="left:328px;top:3304px">COMPANY</h4>
<ul class="abs foot-list" style="left:328px;top:3340px"><li>Contact</li><li>Announcement</li><li>Location</li><li>Feedback</li></ul>
<h4 class="abs foot-h" style="left:517px;top:3304px">CONTACT US</h4>
<div class="abs" style="left:519px;top:3345px;width:230px">
  <div class="contact-row"><svg width="14" height="14" viewBox="0 0 14 14"><rect x="1" y="1" width="12" height="12" rx="2" fill="#444"/><path d="M4 4c0 4 2 6 6 6" stroke="#fff" stroke-width="1.6" fill="none"/></svg>555-014-2290</div>
  <div class="contact-row"><svg width="14" height="14" viewBox="0 0 14 14"><rect x="3" y="1" width="8" height="4" fill="#444"/><rect x="1" y="5" width="12" height="6" rx="1" fill="#444"/><rect x="3" y="9" width="8" height="4" fill="#888"/></svg>555-014-2291</div>
  <div class="contact-row"><svg width="14" height="14" viewBox="0 0 14 14"><rect x="1" y="3" width="12" height="9" fill="#444"/><path d="M1 3l6 5 6-5" stroke="#fff" stroke-width="1.2" fill="none"/></svg><span style="text-decoration:underline">hello@careledger.example</span></div>
  <div class="contact-row"><svg width="14" height="14" viewBox="0 0 14 14"><path d="M7 13C3 8 2 6 2 5a5 5 0 0110 0c0 1-1 3-5 8z" fill="#444"/><circle cx="7" cy="5" r="1.8" fill="#fff"/></svg><span>#4410 Lorem ipsum dolor sit<br>amet, Consectetur</span></div>
</div>
<div class="abs map" role="img" aria-label="Street map showing the office location"></div>
<div class="abs foot-rule"></div>
<p class="abs copy">2016 © CareLedger , All Right Reserved.</p>

</body>
</html>
```